IT Company looking to market towards Dental Offices

I am looking for a full-color design. Using my existing logo. Must have High Res stock photos. The brochure needs to be full page edge to edge design single fold pamphlet style. Content provided. Please see the website in attached Word Doc for more content.

```html
<!DOCTYPE html>
<html lang="en">
<head>
<meta charset="utf-8">
<title>Circuit Guild – Dental IT Brochure</title>
<link href="https://fonts.googleapis.com/css2?family=Lato:ital,wght@0,400;0,700;0,900;1,700&display=swap" rel="stylesheet">
<style>
:root{
  --stage:#a3a3a3;
  --white:#ffffff;
  --band:#1f6cc2;
  --navy:#1b3a8a;
  --deep:#1c3f96;
  --mid:#2563bd;
  --bright:#2d7ad6;
  --ink:#333a44;
  --photo-light:#dfe6ee;
  --photo-stone:#b7b3ad;
  --photo-tech:#4f8fd6;
}
*{margin:0;padding:0;box-sizing:border-box}
html,body{width:923px;height:1200px;overflow:hidden}
body{background:var(--stage);font-family:'Lato',sans-serif;position:relative}
.page{position:absolute;width:410px;overflow:hidden}
.page--cover-left{left:46px;top:62px;height:530px;background:var(--white)}
.page--cover-right{left:468px;top:62px;height:530px;background:var(--white)}
.page--inside-left,.page--inside-right{top:608px;height:530px;background:linear-gradient(160deg,#1d4a9e 0%,#1f55b0 50%,#1a3f92 100%)}
.page--inside-left{left:46px}
.page--inside-right{left:468px}
.art{position:absolute;left:0;top:0}
.footer-band{position:absolute;left:0;bottom:0;width:100%;height:34px;background:var(--band);color:var(--white);font-weight:700;font-size:12px;display:flex;align-items:center;justify-content:center;letter-spacing:.1px}
.cover-copy{position:absolute;left:20px;width:370px;top:412px;font-size:8.6px;line-height:10.6px;color:var(--ink);text-align:center}
.cover-copy p+p{margin-top:8px}
.cover-copy strong{font-weight:700;color:#111}
.brand{position:absolute;left:150px;top:416px;display:flex;align-items:center;gap:10px}
.brand__dot{width:52px;height:52px;border-radius:50%;background:var(--navy)}
.brand__name{font-weight:900;font-size:22px;line-height:22px;color:var(--navy)}
.frame{position:absolute;left:16px;top:14px;width:378px;height:484px;border:3px solid var(--white)}
.lines{position:absolute;left:0;top:0}
.section-title{position:absolute;color:var(--white);font-weight:700;font-size:10.4px;text-transform:uppercase;letter-spacing:.1px}
.body-text{position:absolute;color:var(--white);font-size:7.6px;line-height:9.6px}
.justify{text-align:justify}
.tagline{position:absolute;left:70px;top:213px;color:var(--white);font-weight:700;font-style:italic;font-size:9.6px}
.subhead{position:absolute;left:90px;top:318px;color:var(--white);font-weight:700;font-size:8.4px}
.steps{position:absolute;left:90px;top:336px;list-style:none;color:var(--white)}
.steps li{display:flex;align-items:flex-start;gap:5px;height:27px;font-size:7.6px;line-height:9.6px}
.steps b{font-size:19px;line-height:18px;font-weight:900}
.service-list{position:absolute;left:44px;list-style:none;color:var(--white);font-size:7.6px;line-height:9.6px}
.service-list li::before{content:"\2022";margin-right:5px}
.thumb{position:absolute;left:228px;width:138px;height:95px;border:2px solid var(--white)}
</style>
</head>
<body>

<section class="page page--cover-left">
  <svg class="art" width="410" height="380" viewBox="0 0 410 380">
    <path d="M0,0 H36 C40,200 140,290 240,325 C310,348 370,340 410,318 V372 C330,392 220,378 140,336 C50,288 0,180 0,0 Z" fill="var(--band)"/>
    <path d="M28,0 H410 V318 C360,342 300,340 240,325 C140,290 34,200 28,0 Z" fill="var(--photo-stone)" role="img" aria-label="Photo of a steel bank vault door set in rock"/>
    <circle cx="94" cy="234" r="72" fill="var(--band)"/>
    <circle cx="94" cy="234" r="64" fill="var(--photo-tech)" stroke="var(--white)" stroke-width="3" role="img" aria-label="Photo of hands typing on a laptop with digital overlay"/>
    <circle cx="218" cy="322" r="60" fill="var(--band)"/>
    <circle cx="218" cy="322" r="52" fill="#3b78c6" stroke="var(--white)" stroke-width="3" role="img" aria-label="Photo of network cables plugged into a switch"/>
  </svg>
  <div class="cover-copy">
    <p>Offsite backups for your practice management software made easy and automated. We know how to configure your Dental software to have successful backups every night and be secure, compliant, and verified. Our fully encrypted, enterprise-class offsite backup and recovery solution provides the ultimate protection.</p>
    <p>Get started today at <strong>www.toothsafe.net</strong> We don't charge anything until we have confirmation that your Data has been successfully backed up on our encrypted servers.</p>
  </div>
  <div class="footer-band">www.meadowtechcare.com | 555-014-2290</div>
</section>

<section class="page page--cover-right">
  <svg class="art" width="410" height="400" viewBox="0 0 410 400">
    <path d="M410,0 H374 C370,200 270,290 170,325 C100,348 40,340 0,318 V372 C80,392 190,378 270,336 C360,288 410,180 410,0 Z" fill="var(--band)"/>
    <path d="M382,0 H0 V318 C50,342 110,340 170,325 C270,290 376,200 382,0 Z" fill="var(--photo-light)" role="img" aria-label="Photo of a bright modern dental treatment room with patient chair"/>
    <circle cx="312" cy="240" r="74" fill="var(--band)"/>
    <circle cx="312" cy="240" r="66" fill="var(--photo-tech)" stroke="var(--white)" stroke-width="3" role="img" aria-label="Photo of hands typing on a laptop with digital overlay"/>
    <circle cx="192" cy="322" r="60" fill="var(--band)"/>
    <circle cx="192" cy="322" r="52" fill="#3b78c6" stroke="var(--white)" stroke-width="3" role="img" aria-label="Photo of network cables plugged into a switch"/>
  </svg>
  <div class="brand">
    <span class="brand__dot"></span>
    <span class="brand__name">Circuit<br>Guild</span>
  </div>
  <div class="footer-band">www.meadowtechcare.com | 555-014-2290</div>
</section>

<section class="page page--inside-left" role="img" aria-label="Blue toned server room backdrop">
  <div class="frame"></div>
  <svg class="lines" width="410" height="530" viewBox="0 0 410 530" fill="none" stroke="var(--white)" stroke-width="2">
    <polyline points="130,110 338,110 338,220 156,220"/>
    <polyline points="338,290 71,290 71,479 310,479"/>
  </svg>
  <h2 class="section-title" style="left:70px;top:103px">About Us</h2>
  <p class="body-text justify" style="left:70px;top:126px;width:256px">Circuit Guild offers a proven expertise in Dental Practices. We have trained engineers that specialize in Dental practice management solutions. We can handle supporting your Practice Management Software to installing IOCs, Remote &amp; Sensors, Pano's, X-rays, scanners, pen pads, and more. Being familiar with Digital technology and how your practice runs we are able to predict and plan for your growth by providing the correct configurations the first time and implementing the proper storage solutions you will require.</p>
  <p class="tagline">We know Dental!</p>
  <h2 class="section-title" style="left:90px;top:298px">Ready to make your technology work?</h2>
  <p class="subhead">How To Achieve Technology Bliss for Your Practice</p>
  <ol class="steps">
    <li><b>1.</b><span>Schedule a FREE Network<br>&amp; Technology Evaluation</span></li>
    <li><b>2.</b><span>Receive your Flat Rate Price<br>and Technology Quote</span></li>
    <li><b>3.</b><span>Sit back and let Circuit<br>Guild take care of everything.</span></li>
  </ol>
  <p class="body-text" style="left:90px;top:420px;width:250px">Don't let Technology Departments, Hardware Vendors and Practice Management vendors Point Fingers at each other.</p>
  <p class="body-text" style="left:90px;top:449px;width:250px">We collaborate everything and everyone for you, make one call to us and let us handle your technology.</p>
</section>

<section class="page page--inside-right" role="img" aria-label="Blue toned server room backdrop">
  <div class="frame"></div>
  <h2 class="section-title" style="left:44px;top:89px">Hardware Sales</h2>
  <ul class="service-list" style="top:101px">
    <li>Servers</li><li>Workstations</li><li>Firewalls</li><li>Routers</li><li>Switches</li><li>TVs &amp; Monitors</li><li>Wireless Equipment</li><li>Custom Check-in Workstations</li>
  </ul>
  <div class="thumb" style="top:88px;background:#6a5a52" role="img" aria-label="Photo of computer parts and tools on a workbench"></div>

  <h2 class="section-title" style="left:44px;top:216px">Infrastructure</h2>
  <ul class="service-list" style="top:228px">
    <li>Data &amp; Voice Cable</li><li>HDMI &amp; COAX Video Cable</li><li>TV &amp; Dual Monitor Installation</li><li>Mounting Hardware</li><li>Wireless Installation</li><li>Office Sound Solutions</li><li>Custom Dental Cable</li><li>Video Surveillance</li>
  </ul>
  <div class="thumb" style="top:215px;background:#8c9ab0" role="img" aria-label="Photo of a data centre aisle with server racks and a laptop"></div>

  <h2 class="section-title" style="left:44px;top:342px">Solutions</h2>
  <ul class="service-list" style="top:354px">
    <li>Flat Rate Monthly Support</li><li>Secure Backups with our ToothSafe.net</li><li>Secure Encrypted Emails &amp; X-Rays</li><li>Practice Management Software Experts</li><li>HIPAA Compliance</li><li>Anti-Virus, Anti-Malware and Cyber Security</li><li>Data Recovery</li><li>Cloud Office &amp; Mail Suites</li><li>Phone VOIP &amp; SIP Trunks</li>
  </ul>
  <div class="thumb" style="top:341px;background:#3f6aa6" role="img" aria-label="Photo of two professionals reviewing a laptop in front of a digital screen"></div>
</section>

</body>
</html>
```